Business Card Design

Company is a Commercial Building Company specialising in New Construction and existing refurbishments

Business

Contact Information for Business Card

Derek Halloway
Construction Manager
E Derek@ridgemarkbuilding.com.au
M 0400 215 397
Mail 14 Tarrington Loop Kestrel Point WA 6215

```html
<!DOCTYPE html>
<html lang="en">
<head>
<meta charset="utf-8">
<title>Ridgemark Building &amp; Construction – Business Card</title>
<link rel="stylesheet" href="https://fonts.googleapis.com/css2?family=Saira:wght@400;600&display=swap">
<style>
  :root {
    --backdrop: #2a2a2c;
    --cyan: #12b4cf;
    --cyan-deep: #0fa6c0;
    --cyan-light: #5ccde0;
    --white: #ffffff;
    --paper: #f7f8f8;
    --ink: #2e3440;
    --ink-soft: #3a3f47;
    --font: "Saira", sans-serif;
  }
  html, body {
    margin: 0;
    width: 1200px;
    height: 900px;
    overflow: hidden;
    background: var(--backdrop);
    font-family: var(--font);
  }
  .canvas {
    position: relative;
    width: 1200px;
    height: 900px;
  }
  .card {
    position: absolute;
    left: 320px;
    width: 560px;
    height: 342px;
    border-radius: 26px;
    overflow: hidden;
    box-shadow: 0 10px 30px rgba(0,0,0,0.45);
  }
  .card--front { top: 90px; background: var(--cyan); }
  .card--back { top: 468px; background: var(--paper); }

  .front-decoration {
    position: absolute;
    inset: 0;
    background: linear-gradient(135deg, var(--cyan-light) 0%, var(--cyan) 45%, var(--cyan-deep) 100%);
  }

  .front-brand,
  .back-brand {
    position: absolute;
    right: 40px;
    font-weight: 600;
    line-height: 1;
  }
  .front-brand { top: 58px; color: var(--white); }
  .back-brand { top: 80px; color: var(--ink); }
  .brand-line { display: block; font-size: 24px; letter-spacing: 0.5px; }
  .brand-sub { display: block; font-size: 16px; margin-top: 4px; letter-spacing: 0.5px; }

  .front-web {
    position: absolute;
    right: 40px;
    top: 166px;
    color: var(--white);
    font-weight: 600;
    font-size: 14px;
  }

  .rule {
    position: absolute;
    height: 1px;
    background: var(--ink);
  }
  .rule--top { left: 300px; right: 40px; top: 178px; }
  .rule--title { left: 248px; right: 40px; top: 236px; }

  .person {
    position: absolute;
    left: 40px;
    top: 200px;
  }
  .person-name {
    margin: 0;
    color: var(--cyan);
    font-weight: 600;
    font-size: 21px;
    letter-spacing: 0.5px;
    text-transform: uppercase;
    line-height: 1.1;
  }
  .person-title {
    margin: 2px 0 0;
    color: var(--ink-soft);
    font-size: 17px;
    line-height: 1.2;
  }
  .address {
    position: absolute;
    right: 40px;
    top: 250px;
    text-align: right;
    color: var(--ink-soft);
    font-size: 16px;
    font-style: normal;
    line-height: 1.4;
  }
  .contacts {
    position: absolute;
    left: 40px;
    top: 268px;
    margin: 0;
    padding: 0;
    list-style: none;
    color: var(--ink-soft);
    font-size: 18px;
    line-height: 1.5;
  }
  .contacts li { display: flex; align-items: center; gap: 8px; }
  .contact-icon { width: 20px; height: 20px; flex: none; }
</style>
</head>
<body>
<main class="canvas">

  <section class="card card--front" aria-label="Card front">
    <div class="front-decoration" role="img" aria-label="Decorative brand band pattern"></div>
    <div class="front-brand">
      <span class="brand-line">RIDGEMARK BUILDING</span>
      <span class="brand-sub">&amp; CONSTRUCTION</span>
    </div>
    <div class="front-web">www.ridgemarkbuilding.com.au</div>
  </section>

  <section class="card card--back" aria-label="Card back">
    <div class="back-brand">
      <span class="brand-line">RIDGEMARK BUILDING</span>
      <span class="brand-sub">&amp; CONSTRUCTION</span>
    </div>
    <div class="rule rule--top"></div>

    <div class="person">
      <h1 class="person-name">Derek Halloway</h1>
      <p class="person-title">Construction Manager</p>
    </div>
    <div class="rule rule--title"></div>

    <address class="address">
      Mail 14 Tarrington Loop<br>Kestrel Point WA 6215
    </address>

    <ul class="contacts">
      <li>
        <svg class="contact-icon" viewBox="0 0 20 20" aria-hidden="true">
          <rect x="0" y="0" width="20" height="20" rx="4" fill="var(--cyan)"/>
          <rect x="6.5" y="3.5" width="7" height="13" rx="1.5" fill="none" stroke="var(--white)" stroke-width="1.5"/>
          <circle cx="10" cy="14" r="0.9" fill="var(--white)"/>
        </svg>
        <span>0400 215 397</span>
      </li>
      <li>
        <svg class="contact-icon" viewBox="0 0 20 20" aria-hidden="true">
          <rect x="0" y="0" width="20" height="20" rx="4" fill="var(--cyan)"/>
          <rect x="4" y="6" width="12" height="8" fill="none" stroke="var(--white)" stroke-width="1.4"/>
          <path d="M4 6 L10 11 L16 6" fill="none" stroke="var(--white)" stroke-width="1.4"/>
        </svg>
        <span>Derek@ridgemarkbuilding.com.au</span>
      </li>
    </ul>
  </section>

</main>
</body>
</html>
```